Custom Bladeless LASIK Poster Design Project

I would like a poster whose theme will also be used for future brochures. I would also like it to be created in such a way that it can be part of an in-office branding campaign. Our company already has a logo. We are the premier Ophthalmology group in Orange County, NY specializing in Cataract and Laser Refractive surgery. This particular poster should highlight the advantages to Custom Bladeless LASIK and mention our free consultations and website www.clearviewlumo.com

Would like to make sure the color palette complements the colors in our logo.   Also try incorporating the phrase "Regain your Sight, Regain your Life"

The message should also invite the patient to inquire about more information or to tell a friend about our services

just uploaded the full zip file, please try again.

I just uploaded the full zip file for our logo.  Please let me know if there is still a problem.  Thanks

poster size should be 24" wide 32" high

and able to reduce it to 18"W x 24"H

Thank you 
The designer I choose will also be used in near future for other poster and in office materials highlighting our other services

Reason: I would like to give the other designers that accepted our invitation an opportunity to submit a design.

• attractive young and active male or female model extolling the virtues of eliminating there glasses and contact lenses.

```html
<!DOCTYPE html>
<html lang="en">
<head>
<meta charset="utf-8">
<title>Regain your Sight, Regain your Life — Clearview Lumo Eye Surgeons</title>
<link rel="stylesheet" href="https://fonts.googleapis.com/css2?family=Tinos:ital,wght@0,400;0,700;1,700&display=swap">
<style>
  :root {
    --rose-deep: #d87890;
    --rose-mid: #e59cae;
    --rose-light: #f1c9d3;
    --hair: #6b5a55;
    --skin-light: #f6d9c9;
    --skin-mid: #e8b79e;
    --skin-shadow: #cf9479;
    --wine: #8c1c1c;
    --white: #ffffff;
    --panel: rgba(255, 255, 255, 0.3);
    --ink: #2b2b2b;
  }
  * { box-sizing: border-box; margin: 0; padding: 0; }
  html, body { width: 852px; height: 1200px; overflow: hidden; background: var(--white); }
  body { font-family: "Tinos", "Times New Roman", serif; }

  .poster { position: relative; width: 852px; height: 1200px; overflow: hidden; background: var(--white); }

  .hero {
    position: absolute; left: 0; top: 0; width: 852px; height: 975px;
    background: linear-gradient(90deg, var(--rose-deep) 0%, var(--rose-mid) 25%, var(--rose-light) 45%, var(--rose-light) 100%);
  }
  .hero-model {
    position: absolute; left: 340px; top: 0; width: 512px; height: 975px;
    border-top-left-radius: 120px 260px;
    border-bottom-left-radius: 60px 200px;
    background:
      radial-gradient(ellipse 55% 40% at 62% 40%, var(--skin-light) 0%, rgba(246,217,201,0) 80%),
      radial-gradient(ellipse 40% 20% at 55% 82%, #f2b8b8 0%, rgba(242,184,184,0) 80%),
      linear-gradient(90deg, var(--hair) 0%, var(--skin-shadow) 10%, var(--skin-mid) 30%, var(--skin-light) 65%, var(--skin-mid) 100%);
  }

  .consult-badge {
    position: absolute; left: 67px; top: 38px; width: 236px; height: 236px;
    border: 1.5px solid var(--white); border-radius: 50%;
    display: flex; flex-direction: column; align-items: center; justify-content: center;
    color: var(--white); font-style: italic; font-weight: 700; font-size: 27px; line-height: 1.15;
    text-align: center; transform: rotate(-6deg);
  }
  .consult-badge .badge-key { font-size: 31px; }

  .message-panel {
    position: absolute; left: 35px; top: 423px; width: 602px; height: 517px;
    background: var(--panel); padding: 0 0 0 17px;
  }
  .headline { color: var(--wine); font-weight: 700; font-size: 64px; line-height: 83px; margin-top: -26px; white-space: nowrap; }
  .subhead { color: var(--white); font-weight: 700; font-size: 41px; line-height: 47px; margin-top: 27px; white-space: nowrap; }
  .body-copy { color: var(--white); font-weight: 700; font-size: 30px; line-height: 40px; margin-top: 29px; white-space: nowrap; }

  .brand-band {
    position: absolute; left: 0; top: 975px; width: 852px; height: 225px;
    display: flex; flex-direction: column; align-items: center;
  }
  .brand-name {
    display: flex; align-items: center; gap: 12px; margin-top: 68px;
    color: var(--ink); font-weight: 400; font-size: 27px; letter-spacing: 0.5px;
  }
  .brand-dot { width: 18px; height: 18px; border-radius: 50%; background: var(--wine); }
  .website { color: var(--wine); font-weight: 700; font-size: 66px; line-height: 1; margin-top: 22px; }
</style>
</head>
<body>
<main class="poster">
  <section class="hero">
    <div class="hero-model" role="img" aria-label="Close-up portrait of a smiling young woman with clear brown eyes, no glasses"></div>

    <div class="consult-badge">
      <span>Ask us about a</span>
      <span>complimentary</span>
      <span class="badge-key">LASIK</span>
      <span>consultation</span>
      <span>appointment</span>
    </div>

    <div class="message-panel">
      <h1 class="headline">Regain your Sight,<br>Regain your Life</h1>
      <p class="subhead">Eliminate the need for glasses<br>and contact lenses.</p>
      <p class="body-copy">We specialize in Cataract and<br>Bladeless Laser Vision Correction.<br>Ask our Doctors about the advantages<br>of these exciting procedures.</p>
    </div>
  </section>

  <footer class="brand-band">
    <div class="brand-name"><span class="brand-dot"></span>CLEARVIEW LUMO EYE SURGEONS</div>
    <div class="website">www.clearviewlumo.com</div>
  </footer>
</main>
</body>
</html>
```